Surgical Procedure Room Letterhead

PLEASE DO NOT MAKE YOUR LETTERHEAD SIMILAR TO THE ONE I AM INCLUDING IN MY UPLOADS

Hello! I need my logo used to make a very clean, professional, simple letterhead that has all the pertinent information in it:
Location: 4182 NW 38th Lane, Suite 500
Palmcrest, GA 33967
Phone: 954-218-4650
Fax: 800-642-9082

Can you please put this all on a word document that is easily editable? I will include my practice letterhead as an example ONLY of how easy it should be to write below the letterhead. Please don't make this letterhead the same as the one I am including in this example. They are two separate businesses.

Target Market(s)

Insurance companies

Industry/Entity Type

medical

Requirements
Must have
• classiness, elegance, simplicity
Should not have
• Please don't make your letterhead the same as the one that I included in my uploads

```html
<!DOCTYPE html>
<html lang="en">
<head>
<meta charset="UTF-8">
<title>Meridian Suites Letterhead</title>
<link rel="stylesheet" href="https://fonts.googleapis.com/css2?family=Montserrat:wght@400;500;700&display=swap">
<style>
  :root {
    --gold: #d4ac38;
    --navy: #0d2a57;
    --ink: #1d1d1d;
    --paper: #ffffff;
    --placeholder-start: #e9e9e9;
    --placeholder-end: #f5f5f5;
  }
  * { margin: 0; padding: 0; box-sizing: border-box; }
  html, body { width: 1023px; height: 1200px; overflow: hidden; background: var(--paper); }
  body { font-family: "Montserrat", sans-serif; color: var(--ink); }
  .letterhead { position: relative; width: 1023px; height: 1200px; background: var(--paper); }

  .brand { position: absolute; top: 108px; right: 108px; display: flex; align-items: center; gap: 18px; }
  .brand-mark { width: 54px; height: 54px; border-radius: 50%; background: var(--gold); }
  .brand-name { font-weight: 700; font-size: 46px; color: var(--navy); letter-spacing: 1px; line-height: 1; }

  .sender { position: absolute; left: 107px; top: 270px; }
  .sender-name { font-weight: 700; font-size: 42px; color: var(--gold); line-height: 1.1; }
  .sender-role { font-size: 19px; margin-top: 4px; }

  .address { position: absolute; left: 107px; top: 378px; font-size: 18px; line-height: 18px; font-style: normal; }

  .salutation { position: absolute; left: 110px; top: 440px; font-size: 21px; }
  .date { position: absolute; right: 115px; top: 444px; font-size: 21px; }

  .body-copy { position: absolute; left: 112px; top: 510px; width: 800px; font-size: 15.4px; line-height: 19px; }
  .body-copy p + p { margin-top: 18px; }

  .closing { position: absolute; left: 112px; top: 848px; font-size: 19px; }
  .signature { position: absolute; left: 110px; top: 882px; width: 180px; height: 52px;
    background: linear-gradient(90deg, var(--placeholder-start), var(--placeholder-end)); border-radius: 4px; }

  .contacts { position: absolute; left: 548px; top: 1018px; list-style: none; font-size: 20px; }
  .contacts li { display: flex; align-items: center; gap: 14px; height: 33px; }
  .contacts svg { width: 20px; height: 20px; fill: var(--gold); }
</style>
</head>
<body>
<main class="letterhead">
  <header class="brand">
    <span class="brand-mark"></span>
    <span class="brand-name">Meridian Suites</span>
  </header>

  <section class="sender">
    <h1 class="sender-name">Daniel Hartley</h1>
    <p class="sender-role">Owner</p>
  </section>

  <address class="address">
    4182 NW 38th Lane, Suite 500<br>Palmcrest, GA 33967
  </address>

  <p class="salutation">Dear Sir,</p>
  <p class="date">Sep-28-2024</p>

  <article class="body-copy">
    <p>Lorem ipsum dolor sit amet, consectetur adipiscing elit, sed do eiusmod tempor incididunt ut labore et dolore magna aliqua. Quis ipsum suspendisse ultrices gravida. Risus commodo viverra maecenas accumsan lacus vel facilisis. Lorem ipsum dolor sit amet, consectetur adipiscing elit, sed do eiusmod tempor incididunt ut labore et dolore magna aliqua. Quis ipsum suspendisse ultrices gravida.</p>
    <p>Lorem ipsum dolor sit amet, consectetur adipiscing elit, sed do eiusmod tempor incididunt ut labore et dolore magna aliqua.Quis ipsum suspendisse ultrices gravida. Risus commodo viverra maecenas accumsan lacus vel facilisis. Lorem ipsum dolor sit amet, consectetur adipiscing elit, sed do eiusmod tempor incididunt ut labore et dolore magna aliqua. Quis ipsum suspendisse ultrices gravida. Risus commodo viverra maecenas accumsan lacus vel facilisis.</p>
    <p>Lorem ipsum dolor sit amet, consectetur adipiscing elit, sed do eiusmod tempor incididunt ut labore et dolore magna aliqua. Quis ipsum suspendisse ultrices gravida. Risus commodo viverra maecenas accumsan lacus vel facilisis. Lorem ipsum dolor sit amet, consectetur adipiscing elit, sed do eiusmod tempor incididunt ut labore et dolore magna aliqua. Quis ipsum suspendisse ultrices gravida. Risus commodo viverra maecenas accumsan lacus vel facilisis.</p>
  </article>

  <p class="closing">Rgards</p>
  <div class="signature" role="img" aria-label="Handwritten signature of the sender"></div>

  <ul class="contacts">
    <li>
      <svg viewBox="0 0 24 24" aria-hidden="true"><path d="M6.6 10.8a15.1 15.1 0 0 0 6.6 6.6l2.2-2.2c.3-.3.7-.4 1-.2 1.1.4 2.3.6 3.6.6.6 0 1 .4 1 1V20c0 .6-.4 1-1 1A17 17 0 0 1 3 4c0-.6.4-1 1-1h3.5c.6 0 1 .4 1 1 0 1.3.2 2.5.6 3.6.1.3 0 .7-.2 1z"/></svg>
      <span>954-218-4650</span>
    </li>
    <li>
      <svg viewBox="0 0 24 24" aria-hidden="true"><path d="M6 2h12v5H6zM4 8h16a2 2 0 0 1 2 2v7h-4v5H6v-5H2v-7a2 2 0 0 1 2-2zm4 8v4h8v-4z"/></svg>
      <span>800-642-9082</span>
    </li>
    <li>
      <svg viewBox="0 0 24 24" aria-hidden="true"><path d="M2 5h20v2l-10 6L2 7zm0 4.3 10 6 10-6V19H2z"/></svg>
      <span>info@meridiansuites.com</span>
    </li>
  </ul>
</main>
</body>
</html>
```